Flyer Design Project

We need a flyer design for our lock company called 'Harwell Bolts'. It will be an A5 flyer delivered to local households advertising the benefits of upgrading their existing door locks to higher security , insurance approved ones.
We have the basic text/layout details and are looking forward to receiving your designs to help in the first stage of our new advertising programme.

Target Market(s)

This flyer is intended for general households.
I will be printing the final flyer as double sided, so it can be the same both sides or different each side depending on layout/content etc. any ideas suggestions will be much appreciated.

Industry/Entity Type

Advertising

Requirements
Must have
• HEADING- Something along the lines of 'Security Update', 'Security News' etc.

1) Basic facts- Every 37 seconds a home somewhere in Britain is burgled. In 70% of these burglaries the offenders gain entry through a door.

SUB HEADING- Who has the keys to your home?

TEXT- Over the years keys are lost, lent, borrowed, duplicated or not even handed over from previous owners and/or tennants.
Not only does this make your home more likely to be burgled it may also mean that your insurance policy will not cover you. As part of your insurance requirements you must have approved locks fitted, if they are not this can invalidate your policy.
Upgrading your homes security by upgrading and ensuring your locks are approved is a simple, cost-effective way to ensure not only your homes security but also your peace of mind.
For a free, no-obligation quotation from your local specialists call Harwell Bolts on 01632 960418.

None of this text is essential but, i feel, gets the message across well. If you have other ideas then please feel free to use your own ideas.

At the bottom of the page in small lettering will be;

'Harwell Bolts' is a trading name of Harwell Gates ltd. registered company no. 7316952. VAT #.642 1938 57. 14 Mill Row, Ashcombe.

Our company uses red normally for our name etc. This is by no means a must have but may help, It would also be beneficial to have some photos etc. to help with the text. Any questions please ask.

Nice to have
• I look forward to receiving your ideas and interpretations, i hope this will lead to working with you on our other future projects.
Yours sincerely
Colin Marbury.

```html
<!DOCTYPE html>
<html lang="en">
<head>
<meta charset="utf-8">
<title>Harwell Bolts – Security Alert Flyer</title>
<link href="https://fonts.googleapis.com/css2?family=Oswald:wght@600;700&family=Roboto+Condensed:ital,wght@0,400;0,700;1,400;1,700&display=swap" rel="stylesheet">
<style>
  :root {
    --brand-red: #f25c48;
    --ink: #1a1412;
    --body-ink: #2a2a2a;
    --paper: #ffffff;
    --backdrop: #ffffff;
    --art-top: #c9bfae;
    --art-bottom: #eae6df;
  }
  * { margin: 0; padding: 0; box-sizing: border-box; }
  html, body {
    width: 1200px; height: 900px; overflow: hidden;
    background: var(--backdrop);
  }
  .flyer {
    position: absolute; left: 310px; top: 28px;
    width: 578px; height: 842px;
    background: var(--paper);
    box-shadow: 4px 6px 10px rgba(0,0,0,0.35);
    text-align: center;
  }
  .flyer__heading {
    position: absolute; left: 0; right: 0; top: 14px;
    font-family: "Oswald", sans-serif; font-weight: 700;
    font-size: 86px; line-height: 1; letter-spacing: 0.5px;
    color: var(--brand-red);
  }
  .flyer__facts {
    position: absolute; left: 0; right: 0; top: 122px;
    font-family: "Roboto Condensed", sans-serif; font-style: italic; font-weight: 700;
    font-size: 21px; line-height: 27px; color: var(--ink);
  }
  .flyer__subheading {
    position: absolute; left: 0; right: 0; top: 186px;
    font-family: "Oswald", sans-serif; font-weight: 700;
    font-size: 33px; line-height: 1; color: var(--brand-red);
  }
  .flyer__illustration {
    position: absolute; left: 120px; top: 230px;
    width: 380px; height: 385px;
    background: linear-gradient(180deg, var(--art-top), var(--art-bottom));
    border-radius: 6px;
  }
  .flyer__body {
    position: absolute; left: 40px; right: 40px; top: 622px;
    font-family: "Roboto Condensed", sans-serif; font-size: 12.6px;
    line-height: 16px; color: var(--body-ink);
  }
  .flyer__body p + p { margin-top: 5px; }
  .flyer__body strong { font-style: italic; font-weight: 700; color: var(--ink); }
  .cta {
    position: absolute; left: 27px; top: 734px;
    width: 526px; height: 75px;
    background: var(--brand-red); border-radius: 8px; color: #fff;
  }
  .cta__lead {
    position: absolute; left: 0; right: 0; top: 9px;
    font-family: "Roboto Condensed", sans-serif; font-weight: 700;
    font-size: 17px; letter-spacing: 0.2px;
  }
  .cta__line {
    position: absolute; left: 0; right: 0; top: 28px;
    display: flex; justify-content: center; align-items: center; gap: 8px;
    font-family: "Oswald", sans-serif; font-weight: 700; font-size: 35px; line-height: 42px;
  }
  .cta__icon { width: 38px; height: 38px; }
  .flyer__legal {
    position: absolute; left: 0; right: 0; top: 818px;
    font-family: "Roboto Condensed", sans-serif; font-size: 7.5px; color: var(--body-ink);
  }
</style>
</head>
<body>
  <main class="flyer">
    <h1 class="flyer__heading">Security Alert!</h1>
    <p class="flyer__facts">FACT: Every 37 seconds a home in Britain is burgled.<br>In 70% of these burglaries the offenders gain entry through a door.</p>
    <h2 class="flyer__subheading">Who has the keys to your home?</h2>
    <div class="flyer__illustration" role="img" aria-label="Cartoon burglar in a flat cap and mask creeping with a torch and a ring of keys"></div>
    <div class="flyer__body">
      <p>Over the years keys are lost, lent, borrowed, duplicated or not handed over from previous tennants. Not only does this make your home more likely to be burgled - it may also mean that <strong>your insurance policy will not cover you</strong>. As part of your insurance requirements you must have approved locks fitted, if they are not this can invalidate your policy.</p>
      <p>Upgrading your security by upgrading and ensuring your locks are approved is a simple, cost-effective way to ensure not only your home’s security but also your peace of mind.</p>
    </div>
    <div class="cta">
      <div class="cta__lead">FOR A FREE, NO-OBLIGATION QUOTE CALL</div>
      <div class="cta__line">
        <svg class="cta__icon" viewBox="0 0 24 24" aria-hidden="true"><path fill="#fff" d="M6.6 10.8c1.4 2.8 3.8 5.1 6.6 6.6l2.2-2.2c.3-.3.7-.4 1-.2 1.1.4 2.3.6 3.6.6.6 0 1 .4 1 1V20c0 .6-.4 1-1 1C10.6 21 3 13.4 3 4c0-.6.4-1 1-1h3.5c.6 0 1 .4 1 1 0 1.3.2 2.5.6 3.6.1.3 0 .7-.2 1L6.6 10.8z"/></svg>
        <span>Harwell Bolts 01632 960 418</span>
      </div>
    </div>
    <p class="flyer__legal">'Harwell Bolts' is a trading name of Harwell Gates ltd. registered company no. 7316952. VAT #.642 1938 57. 14 Mill Row, Ashcombe.</p>
  </main>
</body>
</html>
```